UK Online Escort Directory Requires a Redesigned Email Marketing Campaign (4 emails total)

These emails should be designed as marketing emails that will be sent out to approx 10,000 potential customers on a by monthly basis. The designs should be innovative, professional designs that are capable of capturing a readers attention in the blink of an eye.

We have posted this job as our in-house design capabilities are not able to create professional email designs, we therefore require a designer to redesign our email marketing campaign (4 emails total) to a professional level.

The content of the emails will be provided, along with the 5 emails that we are currently sending and the company logo. This should give the potential designer all that they need to redesign the campaign to a professional level.

Please see attached brief for more information on what is required from each individual email.

Target Market(s)

Escorts throughout the UK

Industry/Entity Type

Escort

Font styles to use
Serif
Sans Serif

Requirements
Must have
• Instant recognition of what's being offered.
Nice to have
• Imaginative / inspirational designs.
Should not have
• Any unnecessary wording or text.

```html
<!DOCTYPE html>
<html lang="en">
<head>
<meta charset="utf-8">
<title>VLUK – First Month Free</title>
<link rel="stylesheet" href="https://fonts.googleapis.com/css2?family=Oswald:wght@400;500&family=Open+Sans:wght@300;400;600;700&display=swap">
<style>
  :root {
    --page: #efefef;
    --white: #ffffff;
    --banner: #d9727a;
    --ink: #111111;
    --body-text: #555555;
    --tagline: #3d64a8;
    --wordmark: #b79fd6;
    --rule: #cfcfcf;
    --muted: #8a8a8a;
    --figure: #1c1c1c;
  }
  * { margin: 0; padding: 0; box-sizing: border-box; }
  html, body { width: 936px; height: 1200px; overflow: hidden; }
  body { background: var(--page); font-family: "Open Sans", Arial, sans-serif; color: var(--ink); }
  .email { position: relative; width: 936px; height: 1200px; background: var(--page); }

  .masthead { position: absolute; left: 0; top: 0; width: 936px; height: 182px; background: var(--white); }
  .wordmark { position: absolute; left: 20px; top: 10px; width: 896px; text-align: center;
    font-family: "Open Sans", Arial, sans-serif; font-weight: 300; font-size: 92px; line-height: 1.1;
    color: var(--wordmark); letter-spacing: -1px; white-space: nowrap; }
  .tagline { position: absolute; left: 42px; top: 126px; font-weight: 700; font-size: 22px; color: var(--tagline); }

  .offer-banner { position: absolute; left: 0; top: 182px; width: 936px; height: 96px; }
  .offer-banner svg { position: absolute; left: 0; top: 0; }
  .offer-banner span { position: absolute; left: 0; top: 0; width: 936px; height: 60px; line-height: 60px;
    text-align: center; font-family: "Oswald", sans-serif; font-size: 30px; color: var(--white); }

  .headline { position: absolute; left: 0; top: 290px; width: 936px; text-align: center;
    font-family: "Oswald", sans-serif; font-weight: 400; font-size: 40px; letter-spacing: 0.5px; color: var(--ink); }
  .no-strip { position: absolute; left: 0; top: 356px; width: 936px; text-align: center; white-space: nowrap; }
  .no-strip b { font-family: "Oswald", sans-serif; font-weight: 400; font-size: 78px; line-height: 1; }
  .no-strip small { font-size: 25px; margin: 0 22px 0 8px; }

  .feature-card { position: absolute; left: 36px; top: 496px; width: 866px; height: 281px; background: var(--white);
    border-bottom: 5px double var(--rule); }
  .feature-figure { position: absolute; left: 42px; top: 58px; width: 203px; height: 132px;
    background: linear-gradient(180deg, #2a2a2a, var(--figure)); border-radius: 60px 60px 8px 8px; }
  .feature-title { position: absolute; left: 265px; top: 36px; font-weight: 700; font-size: 28px; }
  .feature-list { position: absolute; left: 293px; top: 86px; list-style: none; }
  .feature-list li { position: relative; font-size: 22px; color: var(--body-text); height: 60px; }
  .feature-list li::before { content: ""; position: absolute; left: -22px; top: 13px; width: 7px; height: 7px;
    border-radius: 50%; background: var(--body-text); }

  .reach { position: absolute; left: 69px; top: 842px; font-size: 22px; }
  .reach strong { font-weight: 700; font-size: 25px; }
  .cta { position: absolute; top: 888px; width: 228px; height: 52px; background: #000; color: var(--white);
    text-align: center; line-height: 52px; font-size: 22px; border-radius: 3px; }
  .cta-browse { left: 126px; }
  .cta-post { left: 583px; height: 50px; line-height: 50px; }
  .cta-url { position: absolute; top: 950px; width: 440px; text-align: center; font-size: 22px; color: var(--ink); }
  .url-browse { left: 20px; }
  .url-post { left: 477px; }

  .signoff { position: absolute; left: 36px; top: 1024px; font-weight: 700; font-size: 26px; }

  .footer { position: absolute; left: 0; top: 1120px; width: 936px; height: 80px; background: var(--white);
    text-align: center; line-height: 80px; font-size: 20px; color: var(--muted); }
</style>
</head>
<body>
<div class="email">
  <header class="masthead">
    <div class="wordmark">velvetlistings-uk.com</div>
    <div class="tagline">The Listing Directory</div>
  </header>

  <div class="offer-banner">
    <svg width="936" height="96" viewBox="0 0 936 96" aria-hidden="true">
      <path d="M0 0H936V60H498C484 60 474 70 468 96C462 70 452 60 438 60H0Z" fill="var(--banner)"/>
    </svg>
    <span>SPECIAL OFFER</span>
  </div>

  <h1 class="headline">FIRST MONTH FREE ON VLUK</h1>
  <p class="no-strip"><b>No</b><small>Credit Card Needed</small><b>No</b><small>Obligation</small></p>

  <section class="feature-card">
    <div class="feature-figure" role="img" aria-label="Black silhouette of a reclining woman"></div>
    <h2 class="feature-title">Your Ad on VLUK</h2>
    <ul class="feature-list">
      <li>Bump your ad to the top as often as you like</li>
      <li>Place your ad in up to three areas</li>
      <li>Change location as often as you want</li>
    </ul>
  </section>

  <p class="reach">Be seen by <strong>15,000 people</strong> a day</p>
  <div class="cta cta-browse">Have a look</div>
  <div class="cta cta-post">Post your free ad</div>
  <div class="cta-url url-browse">www.velvetlistings-uk.com/</div>
  <div class="cta-url url-post">www.velvetlistings-uk.com/post/add</div>

  <p class="signoff">The VLUK Team</p>

  <footer class="footer">Copyright 2016 Velvetlistings-uk.com All Rights Reserved</footer>
</div>
</body>
</html>
```